Pavewell Summit

Im looking for something similar to (brightcoatpaving.com) web site. I really want it to pop!
services we offer:
- Seal Coating
- Crack Filling
- Striping
- Asphalt
- Concrete
- Signage
- Road Grinding
- Grading
- Hydro Blasting
- Recycled asphalt
- Dumpster Pads
- Pressure Washing
- Wheel blocks
- Bollard installation
- Commercial Curbing
- Job site clean up
- Sweeping
- Forestry Clean up
- ADA Compliant work
- Speed bump installation and removal
- Snow removal
- Custom stair sets (Commercial)
Target Market(s)
Parking lot maintenance, asphalt repairs, road grading
Industry/Entity Type
construction, parking lot maintenance
Coding
Coded - Design and coding required
Number of Pages Required
2 page
Look and feel
Each slider illustrates characteristics of the customer's brand and the style your logo design should communicate.

```html
<!DOCTYPE html>
<html lang="en">
<head>
<meta charset="utf-8">
<title>Pavewell Summit</title>
<link href="https://fonts.googleapis.com/css2?family=Anton&family=Poppins:wght@400;500;600;700&display=swap" rel="stylesheet">
<style>
  :root{
    --black:#000;
    --white:#fff;
    --red:#ee1c1c;
    --yellow:#fcc900;
    --ink:#111;
    --nav-active:#e52323;
  }
  *{margin:0;padding:0;box-sizing:border-box}
  html,body{width:1200px;height:622px;overflow:hidden;background:var(--white);font-family:"Poppins",sans-serif}
  .topbar{position:absolute;left:0;top:0;width:1200px;height:44px;background:var(--black);color:var(--white)}
  .contact{position:absolute;left:156px;top:0;height:44px;display:flex;align-items:center;font-size:12px;gap:8px}
  .contact svg{width:10px;height:10px;fill:var(--white)}
  .contact .sep{margin:0 2px}
  .contact .email-icon{margin-right:4px}
  .cta-call,.cta-estimate{position:absolute;top:0;height:44px;display:flex;align-items:center;justify-content:center;font-weight:700;font-size:11px}
  .cta-call{left:699px;width:182px;background:var(--red);color:var(--white)}
  .cta-estimate{left:881px;width:167px;background:var(--yellow);color:var(--ink)}
  .header{position:absolute;left:0;top:44px;width:1200px;height:96px;background:var(--white)}
  .brand{position:absolute;left:160px;top:31px;font-weight:700;font-size:21px;line-height:1.05;color:var(--ink);letter-spacing:1px}
  .brand small{display:block;font-size:21px}
  .nav{position:absolute;right:155px;top:0;height:96px;display:flex;align-items:center;font-size:10px;color:var(--ink);gap:16px}
  .nav a{color:inherit;text-decoration:none}
  .nav a.active{color:var(--nav-active)}
  .hero{position:absolute;left:0;top:140px;width:1200px;height:482px;overflow:hidden;
    background:linear-gradient(180deg,#55606b 0%,#6b6a5f 30%,#4a4a46 55%,#2d2f32 100%)}
  .hero .roller{position:absolute;left:300px;top:60px;width:500px;height:400px;border-radius:40px;
    background:radial-gradient(ellipse at 55% 45%,#a98a2c 0%,#6e5b24 45%,rgba(60,55,40,0) 75%)}
  .hero .shade{position:absolute;inset:0;background:rgba(20,22,28,.35)}
  .hero-title{position:absolute;left:0;width:1200px;top:356px;transform:translateY(-140px);text-align:center;
    font-family:"Anton",sans-serif;font-size:58px;line-height:1;color:var(--white);letter-spacing:.4px}
  .hero-text{position:absolute;left:340px;width:520px;top:304px;text-align:center;color:var(--white);font-size:12px;line-height:15px}
  .hero-button{position:absolute;left:469px;top:392px;width:262px;height:44px;background:var(--yellow);color:var(--ink);
    display:flex;align-items:center;justify-content:center;font-weight:500;font-size:14.5px;letter-spacing:2px;text-decoration:none}
</style>
</head>
<body>
  <div class="topbar">
    <div class="contact">
      <svg viewBox="0 0 24 24"><path d="M6.6 10.8a15 15 0 0 0 6.6 6.6l2.2-2.2c.3-.3.7-.4 1-.2 1.1.4 2.3.6 3.6.6.6 0 1 .4 1 1V20c0 .6-.4 1-1 1A17 17 0 0 1 3 4c0-.6.4-1 1-1h3.5c.6 0 1 .4 1 1 0 1.3.2 2.5.6 3.6.1.3 0 .7-.2 1z"/></svg>
      <span>0800 555 219</span>
      <span class="sep">|</span>
      <svg class="email-icon" viewBox="0 0 24 24"><path d="M2 5h20v2l-10 6L2 7z"/><path d="M2 9l10 6 10-6v10H2z"/></svg>
      <span>info@pavewellsummit</span>
    </div>
    <div class="cta-call">CALL US: 1- 8-888-PAVES</div>
    <div class="cta-estimate">GET A FREE ESTIMATE</div>
  </div>

  <header class="header">
    <div class="brand">PAVEWELL<small>SUMMIT</small></div>
    <nav class="nav">
      <a class="active" href="#">HOME</a><span>|</span>
      <a href="#">ABOUT</a><span>|</span>
      <a href="#">SERVICES</a><span>|</span>
      <a href="#">BLOG</a><span>|</span>
      <a href="#">CONTACT</a>
    </nav>
  </header>

  <section class="hero">
    <div class="roller" role="img" aria-label="Yellow asphalt roller parked on a freshly paved lot beside trucks and buildings"></div>
    <div class="shade"></div>
    <h1 class="hero-title">BEST SEAL AND COATING COPANY</h1>
    <p class="hero-text">Lorem ipsum dolor sit amet, consectetur adipiscing elit, sed do eiusmod tempor incidi-dunt ut labore et dolore magna aliqua. Quis ipsum suspendisse ultrices gravida. Risus commodo viverra maecenas accumsan lacus vel facilisis.</p>
    <a class="hero-button" href="#">REQUEST A FREE ESTIMATE</a>
  </section>
</body>
</html>
```